we can communicate on this, but i want to follow the approach we took on Pell|Quorn & Tillet but i feel the card front needs the black background and the platinum and gold logo. The back? I am open. we can use the same info from PQ&T. Vellum Crest is an enhanced equity investment fund - basically a very exclusive boutique hedge fund that uses only stock options. very advanced things. hope you are interested

Contact Information for Business Card

Dr. Owen T. Brisket, CFA
Scientifique de fusée financière
555.014.2296
TheDoc4793@mailvessel.example

4718 Fennel Brook Way N.
West Fargo, ND 58078

No web site

Colors

Designer to choose colors to be used in the design.

Requirements
Nice to have
• I tend to prefer the most visible applications of the logo to include logo and name, the logo version with a black background and the gold and platinum components separated by the black. I see this working well for a single side (logo and name - this is card front to me).
• I am fairly open to other treatments on the reverse side with the data. To me, it makes sense to have a different color rendition of the logo on the reverse and it may be a muted black tone on tone or an oversized portion that would have spot UV. Or, the reverse may play with colors and layout
Should not have
• Other colors = no no
• Decorative font

```html
<!DOCTYPE html>
<html lang="en">
<head>
<meta charset="utf-8">
<title>Vellum Crest — Business Card</title>
<link rel="stylesheet" href="https://fonts.googleapis.com/css2?family=Montserrat:wght@700&family=Open+Sans:wght@400;600&display=swap">
<style>
  :root {
    --stage: #e9e7e3;
    --card: #141414;
    --gold: #d4a62a;
    --white: #ffffff;
    --text: #eaeaea;
    --rule: #cfcfcf;
  }
  * { margin: 0; padding: 0; box-sizing: border-box; }
  html, body { width: 1200px; height: 1000px; overflow: hidden; }
  body { background: var(--stage); position: relative; font-family: "Open Sans", Arial, sans-serif; }

  .card {
    position: absolute;
    left: 266px;
    width: 666px;
    height: 397px;
    background: var(--card);
    border-radius: 24px;
  }
  .card--front { top: 74px; }
  .card--back { top: 533px; }

  .brand { position: absolute; display: flex; flex-direction: column; align-items: center; }
  .brand__mark { border-radius: 50%; background: var(--gold); }
  .brand__name {
    font-family: "Montserrat", Arial, sans-serif;
    font-weight: 700;
    color: var(--white);
    letter-spacing: 1px;
    white-space: nowrap;
  }
  .card--front .brand { left: 40px; width: 270px; top: 94px; }
  .card--front .brand__mark { width: 120px; height: 120px; }
  .card--front .brand__name { font-size: 34px; margin-top: 26px; }

  .card--back .brand { left: 0; width: 666px; top: 47px; }
  .card--back .brand__mark { width: 144px; height: 144px; }
  .card--back .brand__name { font-size: 48px; margin-top: 40px; }

  .divider {
    position: absolute;
    left: 334px;
    top: 98px;
    width: 2px;
    height: 204px;
    background: var(--rule);
  }

  .contact {
    position: absolute;
    left: 366px;
    top: 116px;
    width: 280px;
    color: var(--text);
    font-size: 16.5px;
    line-height: 24px;
    white-space: nowrap;
  }
  .contact__name { color: var(--gold); font-weight: 600; font-size: 17px; line-height: 26px; }
  .contact__title { margin-bottom: 9px; }
  .contact__address { margin-bottom: 9px; }
  .contact__list { list-style: none; }
  .contact__item { display: flex; align-items: center; gap: 7px; }
  .contact__icon { width: 16px; height: 16px; flex: none; }
</style>
</head>
<body>

<section class="card card--front">
  <div class="brand">
    <div class="brand__mark"></div>
    <div class="brand__name">VELLUM CREST</div>
  </div>

  <div class="divider"></div>

  <div class="contact">
    <div class="contact__name">DR. OWEN T. BRISKET, CFA</div>
    <div class="contact__title">Scientifique de fusée financière</div>
    <div class="contact__address">4718 Fennel Brook Way N.<br>West Fargo, ND 58078</div>
    <ul class="contact__list">
      <li class="contact__item">
        <svg class="contact__icon" viewBox="0 0 16 16"><path fill="#d4a62a" d="M1 6c0-2 3-3 7-3s7 1 7 3v1h-3V5.5H4V7H1zM4 8l1.5-2h5L12 8v5H4z"/><circle cx="8" cy="10" r="1.6" fill="#141414"/></svg>
        <span>555.014.2296</span>
      </li>
      <li class="contact__item">
        <svg class="contact__icon" viewBox="0 0 16 16"><rect x="1" y="3.5" width="14" height="9.5" fill="#d4a62a"/><path d="M1.5 4l6.5 5 6.5-5" fill="none" stroke="#141414" stroke-width="1.2"/></svg>
        <span>TheDoc4793@mailvessel.example</span>
      </li>
    </ul>
  </div>
</section>

<section class="card card--back">
  <div class="brand">
    <div class="brand__mark"></div>
    <div class="brand__name">VELLUM CREST</div>
  </div>
</section>

</body>
</html>
```